Business card design needed

Double sided
Color, unique, elegant

Maybe put this quote somewhere?? But I think it might make it to cluttered?
“The Pilates Method of Body
Conditioning develops the body
uniformly, corrects posture, restores
vitality, invigorates the mind and
elevates the spirit”
- Lionel Hartwick

Industry/Entity Type

Business

Contact Information for Business Card

Marla Trevisick
Pilates Instructor & Personal trainer
Mobile: 0498260543
www.kovira.com.au
email: koviraheal.motion@brintmail.com

```html
<!DOCTYPE html>
<html lang="en">
<head>
<meta charset="utf-8">
<title>Kovira Health and Fitness — Business Card</title>
<link rel="stylesheet" href="https://fonts.googleapis.com/css2?family=Quicksand:wght@400;500;700&display=swap">
<style>
  :root {
    --page: #ecebee;
    --ink: #2a2528;
    --charcoal: #262426;
    --charcoal-light: #3a383a;
    --pink-light: #d7a2d0;
    --pink: #c06fb6;
    --pink-deep: #b461aa;
    --white: #f4f2f4;
  }
  * { box-sizing: border-box; margin: 0; padding: 0; }
  html, body {
    width: 1200px; height: 1200px; overflow: hidden;
    background: var(--page);
    font-family: "Quicksand", sans-serif;
  }
  .canvas {
    width: 1200px; height: 1200px;
    display: flex; flex-direction: column; align-items: center; justify-content: center;
    gap: 60px;
  }
  .card {
    position: relative;
    width: 860px; height: 500px;
    overflow: hidden;
    box-shadow: 0 10px 30px rgba(0,0,0,0.18);
  }

  /* Front */
  .card--front {
    background: linear-gradient(100deg, var(--pink-light) 0%, var(--pink) 40%, var(--pink-deep) 70%);
  }
  .front__panel { position: absolute; inset: 0; width: 100%; height: 100%; }
  .front__contact {
    position: absolute; left: 60px; top: 110px; width: 420px;
    color: var(--ink); text-align: center;
  }
  .contact__name { font-size: 46px; font-weight: 500; text-align: left; margin-bottom: 22px; }
  .contact__label { font-size: 23px; font-weight: 700; }
  .contact__value { font-size: 24px; font-weight: 500; margin-bottom: 18px; }
  .contact__email { font-size: 23px; font-weight: 500; margin-bottom: 22px; }
  .contact__web { font-size: 28px; font-weight: 700; letter-spacing: 1px; }

  .front__role {
    position: absolute; right: 40px; top: 40px; width: 300px;
    color: var(--white); text-align: center;
    font-size: 30px; font-weight: 500; line-height: 1.3;
  }
  .front__brand {
    position: absolute; right: 50px; bottom: 50px; width: 280px;
    display: flex; align-items: center; justify-content: center; gap: 14px;
    color: var(--white); font-size: 62px; font-weight: 400; letter-spacing: 6px;
  }
  .brand__dot { width: 16px; height: 16px; border-radius: 50%; background: var(--pink); }

  /* Back */
  .card--back {
    background: radial-gradient(circle at 70% 20%, var(--charcoal-light) 0%, var(--charcoal) 70%);
    display: flex; flex-direction: column; align-items: center; justify-content: center;
    color: var(--white);
  }
  .back__brand {
    display: flex; align-items: center; gap: 20px;
    font-size: 110px; font-weight: 400; letter-spacing: 12px; line-height: 1;
  }
  .back__brand .brand__dot { width: 24px; height: 24px; }
  .back__tagline { margin-top: 18px; font-size: 38px; font-weight: 500; letter-spacing: 1px; }
</style>
</head>
<body>
<main class="canvas">
  <section class="card card--front" aria-label="Business card front">
    <svg class="front__panel" viewBox="0 0 860 500" preserveAspectRatio="none" aria-hidden="true">
      <defs>
        <linearGradient id="panelShade" x1="0" y1="0" x2="1" y2="1">
          <stop offset="0" stop-color="#2b292b"/>
          <stop offset="1" stop-color="#1f1d1f"/>
        </linearGradient>
      </defs>
      <path d="M500 0 Q430 300 650 500 L860 500 L860 0 Z" fill="url(#panelShade)"/>
    </svg>
    <div class="front__contact">
      <p class="contact__name">Marla Trevisick</p>
      <p class="contact__label">Mobile:</p>
      <p class="contact__value">0498260543</p>
      <p class="contact__label">Email:</p>
      <p class="contact__email">koviraheal.motion@brintmail.com</p>
      <p class="contact__web">www.kovira.com.au</p>
    </div>
    <p class="front__role">Pilates Instructor<br>&amp;<br>Personal trainer</p>
    <div class="front__brand"><span class="brand__dot"></span>KOVIRA</div>
  </section>

  <section class="card card--back" aria-label="Business card back">
    <div class="back__brand"><span class="brand__dot"></span>KOVIRA</div>
    <p class="back__tagline">Health and Fitness</p>
  </section>
</main>
</body>
</html>
```